Website Redesign for a faith-based, not-for-profit health and human services organization

New website design for the Hearthside Faith Outreach House.
- Current site: www.hfohtr.org -
We are looking for a nice clean, simple, friendly-yet-elegant website layout.
Colors are #f5eed5 (cream), #FFFFFF (white), and all logo colors.
Design a layout for home page
Design a layout for general layouts
-layout only no html needed (preferably a high res PSD file format) -
Main menu should be along top with side navigation for submenu, no side menu on home page.
Also would be open to seeing some updated colors on the logo design, currently the colors are slightly outdated. The Vine of Plenty quilt design fits the organization’s mission and the rural farming / Amish-Mennonite-Brethren community around us.

ADDITIONAL PAGES AND MENU STRUCTURE ON NEW SITE

- How to Help
... Volunteer
... Donate Time
... Donate Money
... Donate Supplies
... Current Needs

- Programs

- News & Events
... Upcoming Events
... Upcoming Fundraisers
... Newsletter

- Our Partners

- About Us
... Overview
... Mission
... Staff Directory
... Board of Directors
... Annual Reports

- Contact

Our annual special event is Gather at the Hearth and should be integrated into the home page - see attached logos and banner

Websites with elements we like (from organizations doing similar work), each for a different reason....

1. http://www.kinbridgeway.org
Good design, color, clarity on this site. Multi-dimensional, photos...easy interaction, etc.

2. http://endfamineplainly.org
Quite simple, nothing fancy, but some good basic stuff here, and pretty easy to navigate...

3. http://www.neighborhub.org
Intrigued by the bulletin board design and the way they have their programs broken down to show impact, needs, etc. It has a lot of good information, but is really too verbose, some of the print is too small, etc. Not perfect, but some interesting design elements.

4. http://sharedlarder.org
Site is boring and not very well designed, but it has some of the features that we would like to see at the top, donations, partners, etc.

5. http://www.meadowlarkgrocers.org
Too many listings on the sidebar - needs to be cleaner & simpler, but a lot of good information and we like the way they show volunteer photos on the Our Helpers Shine Bright page...

About
Hearthside Faith Outreach House ("HFOH" or “the Center”) is a faith-based non-for-profit health and human services organization that exists as an outreach of and for the Ostrel Valley Unified School District.
Tagline: Mercy at Work (we work to serve the needs of the ‘least of these’ with compassion).

Mission
Our mission is to see lives transformed and the community enhanced by encouraging the oppressed, defending the cause of the weak and maintaining the rights of the poor - bringing together the resources of a caring community as a demonstration of the good news of Christ.

Company Overview
Hearthside Faith Outreach House works closely with the community in which it serves. A tremendous value is placed upon the partnerships that have formed with caring people within the community and with organizations that share the goal of bringing together resources to help those who need it most. Individuals, volunteers, churches, corporations, foundations, and government sources all pull together to help make our mission possible.

Since 1996 the Hearthside Faith Outreach House has collaboratively worked to see our community enhanced, adapting programs and services to meet the changing needs of the community.

Target Market(s)

people needing assistance in local community

Industry/Entity Type

Government

Requirements
Must have
• Good social button integration
Should not have
• No Find Us page like old website it is not needed

```html
<!DOCTYPE html>
<html lang="en">
<head>
<meta charset="utf-8">
<title>Hearthside Faith Outreach House — Home</title>
<link rel="stylesheet" href="https://fonts.googleapis.com/css2?family=Sorts+Mill+Goudy&family=Lato:wght@300;400&family=Arimo:ital,wght@0,400;0,700;1,700&family=Ubuntu:wght@500&display=swap">
<style>
:root{
  --paper:#f1f0ee;
  --red:#8e1b12;
  --red-deep:#a3160b;
  --red-dark:#6d0f08;
  --green:#1d4d22;
  --gold:#b38e2a;
  --ink:#333;
  --ink-soft:#555;
  --line:#d6d3cf;
}
*{box-sizing:border-box;margin:0;padding:0}
html,body{width:994px;height:1200px;overflow:hidden}
body{position:relative;background:var(--paper);font-family:Arimo,Arial,sans-serif;color:var(--ink)}
.abs{position:absolute}

/* header */
.site-header{left:0;top:0;width:994px;height:161px;background:linear-gradient(#f4f3f1,#ebe9e6)}
.brand{left:118px;top:10px;display:flex;align-items:flex-start;gap:10px}
.brand-mark{width:82px;height:82px;background:var(--red);margin-top:8px}
.brand-name{font-family:"Sorts Mill Goudy",Georgia,serif;color:var(--gold);font-size:19px;line-height:19px}
.social{top:13px;display:flex;gap:12px;left:804px}
.social span{width:28px;height:28px;border-radius:6px;background:#b8872f}
.tagline{left:451px;top:70px;font-family:Lato,sans-serif;font-weight:300;font-size:30px;color:var(--gold);white-space:nowrap}
.tagline em{font-style:normal;color:var(--red)}
.rule{left:105px;top:112px;width:778px;height:1px;background:var(--line)}
.main-nav{left:178px;top:118px;height:38px;display:flex;font-family:Lato,sans-serif;font-size:12px;color:#333}
.main-nav a{color:inherit;text-decoration:none;display:flex;align-items:center;justify-content:center;border-left:1px solid var(--line);height:38px;white-space:nowrap}
.main-nav a:last-child{border-right:1px solid var(--line)}
.main-nav .current span{background:var(--red);color:#fff;padding:7px 18px}

/* body */
.red-band{left:0;top:161px;width:994px;height:934px;background:radial-gradient(ellipse at center,var(--red-deep),#7c0e07)}
.content{left:96px;top:161px;width:802px;height:934px;background:var(--paper)}
.hero{left:108px;top:175px;width:780px;height:279px;background:linear-gradient(160deg,#8a4a3a 0%,#c8bfb6 35%,#e9e6e2 60%,#9ea48a 100%)}
.hero-caption{left:118px;top:327px;width:369px;height:106px;background:rgba(240,238,236,.82);padding:16px 0 0 10px;font-family:"Sorts Mill Goudy",Georgia,serif;color:var(--red);font-size:27px;line-height:28px;white-space:nowrap}
.hero-caption strong{color:var(--green);font-size:43px;font-weight:700;font-family:Georgia,serif}
.hero-shadow{left:140px;top:456px;width:716px;height:14px;background:radial-gradient(ellipse at top,rgba(0,0,0,.28),transparent 70%)}

.section-title{height:43px;background:var(--red);color:#fff;font-family:"Sorts Mill Goudy",Georgia,serif;font-size:23px;font-weight:400;line-height:43px;display:flex;align-items:center;gap:8px;padding-left:8px;white-space:nowrap;overflow:hidden}
.section-title .icon{width:28px;height:28px;background:#fff;border-radius:5px;display:flex;align-items:center;justify-content:center;flex:none}
.col-divider{width:0;border-left:1px dotted #c4c0bb}
.photo-frame{background:#fff;border:1px solid #ddd;padding:6px;box-shadow:0 1px 3px rgba(0,0,0,.12)}
.photo-frame div{width:100%;height:100%}
.teaser{font-size:10px;line-height:15px;color:var(--ink-soft);text-align:justify;letter-spacing:.3px}
.read-more{background:var(--green);color:#fff;font-size:9px;padding:5px 5px;display:inline-block}

.event-item{display:flex;gap:6px;border-bottom:1px solid var(--line)}
.event-thumb{width:87px;height:48px;background:linear-gradient(#f4efe3,#e2d5b6);border:1px solid #ddd;flex:none;margin-top:4px}
.event-text{font-size:10px;line-height:15px;color:var(--ink);letter-spacing:.1px}
.event-date{display:block;text-align:right;color:var(--red);font-weight:700;font-size:9px;margin-top:1px}

.h-rule{left:106px;top:767px;width:778px;height:1px;background:var(--line)}
.upcoming-card{background:#fff;border:1px solid #e0ddd9;border-radius:6px;padding:12px 15px 0 10px;display:flex;gap:12px}
.upcoming-card .thumb{width:74px;height:78px;flex:none;margin-top:1px}
.upcoming-card h3{font-family:Ubuntu,sans-serif;font-weight:500;font-size:14px;color:#444;margin-bottom:6px;white-space:nowrap}
.upcoming-card .dated{color:var(--red);font-weight:700;font-style:italic;font-size:10px;margin:0 0 4px 2px}
.upcoming-card p{font-size:10px;line-height:15px;color:var(--ink-soft);text-align:justify;letter-spacing:.2px}

.optin{left:662px;top:827px;width:212px;height:183px;background:linear-gradient(#3c8a33,#1c4a1e)}
.optin-intro{background:#3a3a3a;color:#eee;font-size:9.5px;line-height:13px;padding:9px 8px;height:47px;letter-spacing:.2px}
.optin-field{margin:13px 0 0 13px;width:184px;height:30px;border:1px solid #6b9d62;border-radius:14px;background:rgba(20,60,20,.45);color:#b9ceb4;font-size:10px;padding:8px 11px;letter-spacing:.4px}
.optin-btn{position:absolute;right:17px;bottom:15px;width:83px;height:25px;border-radius:8px;background:linear-gradient(#444,#111);border:1px solid #aaa;color:#fff;font-size:11px;text-align:center;line-height:23px}
.donate{left:669px;top:1027px;width:200px;height:54px;border-radius:9px;background:linear-gradient(#a52a1f,var(--red-dark));color:#fff;font-family:Georgia,serif;font-weight:700;font-size:26px;text-align:center;line-height:54px;box-shadow:0 1px 2px rgba(0,0,0,.3);white-space:nowrap}

.site-footer{left:0;top:1095px;width:994px;height:105px;background:linear-gradient(#efeeec,#e6e4e1)}
.footer-info{left:106px;top:1129px;font-size:10px;line-height:17.5px;color:#333;letter-spacing:.2px;white-space:nowrap}
.partner-badge{top:1126px;height:46px;background:#2a2a2a}
</style>
</head>
<body>

<header class="site-header abs">
  <div class="brand abs">
    <span class="brand-mark"></span>
    <div class="brand-name">Hearthside<br>Faith<br>Outreach<br>House</div>
  </div>
  <div class="social abs">
    <span role="img" aria-label="Social network link"></span>
    <span role="img" aria-label="Social network link"></span>
  </div>
  <div class="tagline abs">Mercy at Work <em>Since 1996</em></div>
  <div class="rule abs"></div>
  <nav class="main-nav abs">
    <a class="current" style="width:110px"><span>Home</span></a>
    <a style="width:106px">How to Help</a>
    <a style="width:99px">Programs</a>
    <a style="width:113px">Our Partners</a>
    <a style="width:103px">About Us</a>
    <a style="width:108px">Contact Us</a>
  </nav>
</header>

<div class="red-band abs"></div>
<main class="content abs"></main>

<div class="hero abs" role="img" aria-label="Group photo of volunteers in matching white shirts outside a brick building"></div>
<div class="hero-caption abs">Building a Better Community<br>for <strong>16 years!</strong></div>
<div class="hero-shadow abs"></div>

<section class="abs" style="left:114px;top:492px;width:227px">
  <h2 class="section-title"><span class="icon"><svg width="18" height="18" viewBox="0 0 18 18"><rect x="2" y="2" width="11" height="14" fill="none" stroke="#777"/><path d="M7 14 L16 3" stroke="#8e1b12" stroke-width="2"/></svg></span>Featured Articles</h2>
  <div class="photo-frame" style="margin:12px 0 0 4px;width:222px;height:107px"><div role="img" aria-label="Volunteer cooks preparing trays of food" style="background:linear-gradient(135deg,#5a6570,#c9b49a 55%,#efeae2)"></div></div>
  <p class="teaser" style="margin:17px 0 0 6px;width:215px">Lorem ipsum dolor sit amet, consectetur adipiscing elit. Proin sed ipsum tortor. Nam aliquam lacinia elementum.</p>
  <span class="read-more" style="margin:15px 0 0 8px">Read more »</span>
</section>
<div class="col-divider abs" style="left:361px;top:497px;height:262px"></div>

<section class="abs" style="left:383px;top:492px;width:227px">
  <h2 class="section-title"><span class="icon"><svg width="18" height="18" viewBox="0 0 18 18"><circle cx="9" cy="9" r="7" fill="#8e1b12"/><rect x="7.5" y="4" width="3" height="6" rx="1.5" fill="#fff"/><rect x="8.5" y="10" width="1" height="4" fill="#fff"/></svg></span>Current Needs</h2>
  <div class="photo-frame" style="margin:12px 0 0 3px;width:222px;height:107px"><div role="img" aria-label="Colleagues working together at a laptop" style="background:linear-gradient(135deg,#e6d8c8,#cfd6dc 50%,#6f7880)"></div></div>
  <p class="teaser" style="margin:17px 0 0 5px;width:216px">Current is to see lives transformed and the community enhanced by encouraging the oppressed, defending the cause...</p>
  <span class="read-more" style="margin:15px 0 0 6px">Read more »</span>
</section>
<div class="col-divider abs" style="left:632px;top:497px;height:262px"></div>

<section class="abs" style="left:652px;top:492px;width:228px">
  <h2 class="section-title"><span class="icon" style="background:transparent"><svg width="24" height="24" viewBox="0 0 24 24"><rect x="3" y="4" width="18" height="17" fill="#fff"/><rect x="3" y="4" width="18" height="4" fill="#d44"/><path d="M6 12h12M6 16h12" stroke="#bbb"/></svg></span>Featured Events</h2>
  <div class="event-item" style="margin-top:24px;padding-bottom:12px">
    <div class="event-thumb" role="img" aria-label="Gather at the Hearth event banner"></div>
    <div class="event-text">Thank You To Brookline Timber And Everyone Who Helped Make Our First Farm-to-table Event A Success!<span class="event-date">Aug. 10th 2013</span></div>
  </div>
  <div class="event-item" style="margin-top:22px;border:0">
    <div class="event-thumb" role="img" aria-label="Gather at the Hearth event banner"></div>
    <div class="event-text">Thank You To Brookline Timber And Everyone Who Helped Make Our First Farm-to-table Event A Success!<span class="event-date">Aug. 10th 2013</span></div>
  </div>
</section>

<div class="h-rule abs"></div>

<h2 class="section-title abs" style="left:124px;top:778px;width:227px"><span class="icon" style="width:26px;height:26px"><svg width="18" height="18" viewBox="0 0 18 18"><path d="M3 15 L9 9" stroke="#222" stroke-width="2"/><path d="M3 7 A8 8 0 0 0 11 15 Z" fill="#222"/><path d="M10 4a4 4 0 0 1 4 4M10 1a7 7 0 0 1 7 7" fill="none" stroke="#222"/></svg></span>Upcoming Events</h2>
<article class="upcoming-card abs" style="left:123px;top:826px;width:493px;height:126px">
  <div class="thumb" role="img" aria-label="Silhouette with raised arms against a sunset" style="background:linear-gradient(#7a5a2c,#e0a23a 70%,#3a2a14)"></div>
  <div>
    <h3>Etiam adipiscing imperdiet mauris at dignissim.</h3>
    <p class="dated">Dated : 01-02-13</p>
    <p>Maecenas eleifend libero nisl, sed scelerisque ligula. Sed lobortis nisl a ligula tincidunt ut semper ipsum eleifend. Nunc enim leo, auctor pellentesque vestibulum in, semper eget quam. Suspendisse aliquet neque eget erat blandit ac dapibus dui vestibulum...</p>
  </div>
</article>
<article class="upcoming-card abs" style="left:123px;top:965px;width:493px;height:126px">
  <div class="thumb" role="img" aria-label="Person gazing at the sky by the sea" style="height:70px;background:linear-gradient(#9cc0dc,#d9c4a6 60%,#4b6f8a)"></div>
  <div>
    <h3>Etiam adipiscing imperdiet mauris at dignissim.</h3>
    <p class="dated">Dated : 01-02-13</p>
    <p style="margin-top:6px">Maecenas eleifend libero nisl, sed scelerisque ligula. Sed lobortis nisl a ligula tincidunt ut semper ipsum eleifend. Nunc enim leo, auctor pellentesque vestibulum in, semper eget quam. Suspendisse aliquet neque eget erat blandit ac dapibus dui vestibulum...</p>
  </div>
</article>
<div class="col-divider abs" style="left:637px;top:795px;height:295px"></div>

<h2 class="section-title abs" style="left:652px;top:778px;width:227px;gap:12px"><span class="icon" style="width:26px;height:26px"><svg width="18" height="18" viewBox="0 0 18 18"><circle cx="5" cy="9" r="3.5" fill="none" stroke="#777" stroke-width="2"/><path d="M8 9h9M14 9v3M16 9v2" stroke="#777" stroke-width="2"/></svg></span>Optin Here</h2>
<form class="optin abs">
  <p class="optin-intro">Lorem ipsum dolor sit amet, consectetur adipiscing elit. Proin sed ipsum tortor.</p>
  <div class="optin-field">Your Name</div>
  <div class="optin-field" style="margin-top:12px">Your Email</div>
  <div class="optin-btn">Continue</div>
</form>
<div class="donate abs">Donate Now</div>

<footer class="site-footer abs"></footer>
<div class="footer-info abs">
  Home &nbsp;|&nbsp; Programs &nbsp;|&nbsp; Events &nbsp;|&nbsp; Contact<br>
  Hearthside Faith Outreach House &nbsp; 48 North Alder Lane &nbsp; Marlowe &nbsp; IN &nbsp; 40012<br>
  Ph.: &nbsp;555.014.2290 &nbsp;Fax 555.014.7731
</div>
<div class="partner-badge abs" role="img" aria-label="Partner badge" style="left:654px;width:114px"></div>
<div class="partner-badge abs" role="img" aria-label="Partner badge" style="left:772px;width:116px;background:#fff;border:2px solid #222"></div>

</body>
</html>
```